Business card for Drone Aerial

I need a business card designed keeping in mind I want to do post cards also with a similar design.
Both sides of the card would be cool.
I have a vortel 8 max and would like a picture of it on the front of the card. Similar to one I attached.
I really like the look of a drone in the air and the background pic a little blurry. I attached a few images as IDEAS.
Some special things I want to be on the card additional to the normal business card info:
"Aerial Photography" or "Low Altitude Aerial Photography"?
"KTO# 58203917"

I like modern and creative. My Favorite color is blue and I like blue on white.
I do not have a business name and am not going to have one. When they read "Aerial Photography" and see the drone and image they will know what the card is for.

FYI, The attached pictures are just images from pixelgrove and just samples/ideas.

Target Market(s)

Real estate, construction, events

Industry/Entity Type

Business

Contact Information for Business Card

Also Definitely want to contain, my name, my number and email address.

Requirements
Must have
• "KTO# 58203917"
• "Aerial Photography"

```html
<!DOCTYPE html>
<html lang="en">
<head>
<meta charset="utf-8">
<title>Aerial Photography Business Card</title>
<link href="https://fonts.googleapis.com/css2?family=Roboto:wght@400;500;700&display=swap" rel="stylesheet">
<style>
  :root {
    --backdrop: #e6e8ec;
    --card-white: #ffffff;
    --band-blue: #2b5fae;
    --band-blue-light: #4d7fcb;
    --band-blue-dark: #1f4c94;
    --sky-top: #9aa6c9;
    --sky-mid: #8f9cc6;
    --city-blue: #5e7fb8;
    --city-pink: #b79bb6;
    --front-band: rgba(60, 112, 196, 0.72);
    --drone-white: #f2f4f7;
    --drone-grey: #c3cad6;
    --text-light: #ffffff;
    --text-soft: #e4ecf8;
  }
  * { margin: 0; padding: 0; box-sizing: border-box; }
  html, body {
    width: 1200px; height: 871px; overflow: hidden;
    background: var(--backdrop);
    font-family: "Roboto", Arial, sans-serif;
  }
  .stage { position: relative; width: 1200px; height: 871px; }

  .card {
    position: absolute; width: 630px; height: 360px;
    overflow: hidden; border-radius: 2px;
    box-shadow: 0 10px 28px rgba(20, 30, 50, 0.25);
  }

  /* Front side */
  .card--front { left: 100px; top: 50px; }
  .front-photo {
    position: absolute; inset: 0;
    background: linear-gradient(180deg, var(--sky-top) 0%, var(--sky-mid) 35%, var(--city-blue) 62%, var(--city-pink) 82%, #8a93b8 100%);
  }
  .front-drone {
    position: absolute; left: 400px; top: 58px; width: 200px; height: 120px;
    border-radius: 14px;
    background: linear-gradient(180deg, var(--drone-white) 0%, var(--drone-grey) 100%);
    opacity: 0.92;
  }
  .front-band {
    position: absolute; left: 0; right: 0; top: 142px; height: 84px;
    background: var(--front-band);
    display: flex; align-items: center; padding-left: 62px;
  }
  .tagline {
    color: var(--text-soft); font-size: 24px; font-weight: 700;
    letter-spacing: 0.3px;
  }

  /* Back side */
  .card--back { left: 470px; top: 460px; background: var(--card-white); }
  .back-band { position: absolute; inset: 0; width: 100%; height: 100%; }
  .back-drone {
    position: absolute; left: 480px; top: 92px; width: 150px; height: 130px;
    border-radius: 14px 0 0 14px;
    background: linear-gradient(180deg, var(--drone-white) 0%, var(--drone-grey) 100%);
    opacity: 0.9;
  }
  .holder-name {
    position: absolute; left: 60px; top: 116px;
    color: var(--text-light); font-size: 30px; font-weight: 500;
  }
  .contact-list {
    position: absolute; left: 290px; top: 112px;
    list-style: none; color: var(--text-light);
    font-size: 15px; font-weight: 500;
  }
  .contact-item { display: flex; align-items: center; height: 26px; white-space: nowrap; }
  .contact-icon { width: 16px; height: 16px; margin-right: 16px; flex: none; }
  .licence { padding-left: 32px; }
</style>
</head>
<body>
<main class="stage">

  <section class="card card--front" aria-label="Card front">
    <div class="front-photo" role="img" aria-label="Soft-focus city skyline at dusk"></div>
    <div class="front-drone" role="img" aria-label="White vortel 8 max quadcopter drone hovering in the sky"></div>
    <div class="front-band">
      <h1 class="tagline">Low Altitude Aerial Photography</h1>
    </div>
  </section>

  <section class="card card--back" aria-label="Card back">
    <svg class="back-band" viewBox="0 0 630 360" preserveAspectRatio="none" aria-hidden="true">
      <defs>
        <linearGradient id="bandFill" x1="0" y1="0" x2="1" y2="1">
          <stop offset="0" stop-color="#3a6bb8"/>
          <stop offset="0.45" stop-color="#2b5fae"/>
          <stop offset="1" stop-color="#1f4c94"/>
        </linearGradient>
      </defs>
      <polygon points="0,80 250,80 270,64 630,64 630,300 330,300 310,290 0,290" fill="url(#bandFill)"/>
    </svg>
    <div class="back-drone" role="img" aria-label="White vortel 8 max quadcopter drone in flight"></div>

    <h2 class="holder-name">Dara Whitlow</h2>

    <ul class="contact-list">
      <li class="contact-item">
        <svg class="contact-icon" viewBox="0 0 16 16" aria-hidden="true"><path d="M2 6 Q8 1 14 6 L12 8 L10 6 L6 6 L4 8 Z M4 9 H12 V14 H4 Z" fill="none" stroke="#fff" stroke-width="1.3"/></svg>
        555 014 7720
      </li>
      <li class="contact-item">
        <svg class="contact-icon" viewBox="0 0 16 16" aria-hidden="true"><rect x="4.5" y="1.5" width="7" height="13" rx="1.2" fill="none" stroke="#fff" stroke-width="1.3"/><line x1="7" y1="12.3" x2="9" y2="12.3" stroke="#fff" stroke-width="1.2"/></svg>
        555 014 7721
      </li>
      <li class="contact-item">
        <svg class="contact-icon" viewBox="0 0 16 16" aria-hidden="true"><rect x="1.5" y="3.5" width="13" height="9" fill="none" stroke="#fff" stroke-width="1.3"/><path d="M1.5 3.5 L8 9 L14.5 3.5" fill="none" stroke="#fff" stroke-width="1.3"/></svg>
        dara@whitlowair.net
      </li>
      <li class="contact-item licence">KTO# 58203917</li>
    </ul>
  </section>

</main>
</body>
</html>
```